Financial Services Business Card Design

We are a financial services company Based in London, offering Short term Funding Solutions for companies, raising anywhere between £20,000 and £25million pounds.

The Card must have a professional look as it is going to be handed out to professionals I.E Solicitors, Accountants, Company directors and Business owners.

See Attached our company Logo

Industry/Entity Type

Business

Contact Information for Business Card

Lewis Thorncroft
Suite 41
R K House
Bramblecote Lane
Ashdene
HP19 4QX

```html
<!DOCTYPE html>
<html lang="en">
<head>
<meta charset="utf-8">
<title>Kestrel Capital – Business Card</title>
<link href="https://fonts.googleapis.com/css2?family=Montserrat:wght@700;800&family=Open+Sans:wght@400;600&display=swap" rel="stylesheet">
<style>
  :root {
    --backdrop: #2e2e2e;
    --card: #060606;
    --card-edge: #141414;
    --brand-green: #2fa84f;
    --text-white: #f2f2f2;
  }
  * { margin: 0; padding: 0; box-sizing: border-box; }
  html, body {
    width: 1200px; height: 900px; overflow: hidden;
    background: var(--backdrop);
  }
  .canvas { position: relative; width: 1200px; height: 900px; }
  .card {
    position: absolute;
    width: 595px; height: 340px;
    background: var(--card);
    border: 1px solid var(--card-edge);
    border-radius: 22px;
    box-shadow: 0 18px 40px rgba(0,0,0,0.55);
    overflow: hidden;
  }
  .card--front { left: 110px; top: 70px; }
  .card--back { left: 495px; top: 490px; }

  .front-brand {
    position: absolute; inset: 0;
    display: flex; align-items: center; justify-content: center;
  }
  .front-brand__name {
    font-family: "Montserrat", sans-serif;
    font-weight: 800;
    font-size: 40px;
    letter-spacing: 1px;
    color: var(--brand-green);
  }

  .back-brand {
    position: absolute; right: 36px; top: 48px;
    display: flex; align-items: center; gap: 12px;
  }
  .back-brand__dot {
    width: 16px; height: 16px; border-radius: 50%;
    background: var(--brand-green);
  }
  .back-brand__name {
    font-family: "Montserrat", sans-serif;
    font-weight: 800;
    font-size: 30px;
    color: var(--text-white);
  }

  .contact {
    position: absolute; left: 42px; bottom: 34px;
    width: 310px;
    font-family: "Open Sans", sans-serif;
    color: var(--text-white);
    font-size: 15px; line-height: 1.45;
    text-align: center;
  }
  .contact__name {
    display: flex; align-items: center; justify-content: center; gap: 8px;
    font-family: "Montserrat", sans-serif;
    font-weight: 700; font-size: 21px; letter-spacing: 2px;
    color: var(--brand-green);
    margin-bottom: 6px;
  }
  .contact__bullet {
    width: 9px; height: 9px; border-radius: 50%;
    background: var(--text-white);
  }
  .contact__line { display: flex; align-items: center; justify-content: center; gap: 7px; }
  .contact__icon { width: 12px; height: 12px; flex: none; }
</style>
</head>
<body>
<main class="canvas">
  <section class="card card--front" aria-label="Card front">
    <div class="front-brand">
      <span class="front-brand__name">KESTREL CAPITAL</span>
    </div>
  </section>

  <section class="card card--back" aria-label="Card back">
    <div class="back-brand">
      <span class="back-brand__dot"></span>
      <span class="back-brand__name">KESTREL CAPITAL</span>
    </div>

    <div class="contact">
      <div class="contact__name">
        <span class="contact__bullet"></span>
        LEWIS THORNCROFT
        <span class="contact__bullet"></span>
      </div>
      <p>Suite 41, R K House,</p>
      <p>Bramblecote Lane, Ashdene, HP19 4QX</p>
      <p class="contact__line">
        <svg class="contact__icon" viewBox="0 0 24 24" aria-hidden="true">
          <path fill="#2fa84f" d="M6.6 10.8a15.1 15.1 0 0 0 6.6 6.6l2.2-2.2a1 1 0 0 1 1-.25 11.4 11.4 0 0 0 3.6.57 1 1 0 0 1 1 1V20a1 1 0 0 1-1 1A17 17 0 0 1 3 4a1 1 0 0 1 1-1h3.5a1 1 0 0 1 1 1c0 1.25.2 2.45.57 3.570a1 1 0 0 1-.25 1z"/>
        </svg>
        +44 1632 960 014
      </p>
      <p class="contact__line">
        <svg class="contact__icon" viewBox="0 0 24 24" aria-hidden="true">
          <rect x="2.5" y="5" width="19" height="14" rx="1.5" fill="none" stroke="#2fa84f" stroke-width="2"/>
          <path d="M3 6l9 7 9-7" fill="none" stroke="#2fa84f" stroke-width="2"/>
        </svg>
        info@kestrelcapital.co.uk
      </p>
    </div>
  </section>
</main>
</body>
</html>
```